"Trelvix" printing shop

-The design must be based around the attached HPID (home page information design) called "Trelvix - HPID".

The table boxes are just for approximate placement of information – you DON'T have to box everything in and you can arrange these. All fonts used in the HPID are only examples - you can use any Zarvel font you wish.

- Information only is in orange text. Copy to go on the design in black text. Some instructions are in the HPID. Please be creative!

-The design needs to be modern. Colours are to be consistent with their new logo or complement it. Keep it clean and simple, you don't need to use lots of colours. Use lots of white.

- images / icons for the site need to be relevant and high quality, but they must also be free images or icons. I have attached a few examples that could be used.

Width of content will be 1100 pixels when implemented as a web page. Header height (without nav bar) 150-200 pixels.

If your design is chosen the winning PSD file will have to be provided as follows…
1. Canvas size of 2000px x 2000px - 72ppi in Adobe Photoshop (CS5 compatible)
2. Width of content section is 1100px wide - centered in the canvas
3. Any button rollovers/hovers in the PSD as hidden layers.
4. All fonts used must be Zarvel fonts.
5. You will need to supply the chosen home page plus one example page (example page as a style guide for how all other pages will look). Example page is only the header and navigational bar at the top, an empty sector in the middle with a column (190 px wide) which can be left or right aligned which means the main sector is 910 pixels wide, and then the footer at the bottom of the page

Checklist - http://plumvoratelist.example/

Examples of some websites that have great design... don't copy them please but they are similar in look to what we are after....
http://www.brindolfa.example/

• Drop shadows, comic sans font

```html
<!DOCTYPE html>
<html lang="en">
<head>
<meta charset="utf-8">
<title>Trelvix – Printing &amp; Photocopying</title>
<link rel="stylesheet" href="https://fonts.googleapis.com/css2?family=Questrial&family=Oswald:wght@400;500&family=Nunito:wght@900&family=Lato:wght@400&display=swap">
<style>
:root{
  --brand:#353896;
  --brand-soft:#ececf8;
  --green:#8cc63f;
  --white:#ffffff;
  --accent:#f2c12e;
  --hero-dark:#5f5f5f;
  --hero-light:#bdbdbd;
}
*{margin:0;padding:0;box-sizing:border-box}
html,body{width:1000px;height:1200px;overflow:hidden;background:var(--white)}
body{position:relative;font-family:"Questrial",sans-serif;color:var(--brand)}

.site-header{position:absolute;top:0;left:0;width:1000px;height:65px}
.brand{position:absolute;left:455px;top:12px;display:flex;align-items:center;gap:8px}
.brand-dot{width:36px;height:36px;border-radius:50%;background:var(--brand)}
.brand-name{font-family:"Questrial",sans-serif;font-size:28px;color:var(--brand);letter-spacing:.5px}
.contact{position:absolute;left:731px;top:18px;font-size:8px;line-height:9px;color:var(--brand)}
.contact-row{display:flex;align-items:flex-start;gap:3px;margin-bottom:6px}
.contact svg{flex:none}

.main-nav{position:absolute;top:65px;left:0;width:1000px;height:25px;background:var(--brand)}
.main-nav ul{list-style:none;position:absolute;left:201px;width:615px;top:0;height:22px;display:flex;justify-content:space-between;align-items:center}
.main-nav li{white-space:nowrap}
.main-nav a{font-family:"Oswald",sans-serif;font-size:7px;letter-spacing:-0.1px;color:var(--white);text-decoration:none;text-transform:uppercase}
.main-nav a.lower{text-transform:none;font-size:8px}
.main-nav a.current{color:var(--accent)}

.hero{position:absolute;top:90px;left:0;width:1000px;height:400px}
.hero-photo{position:absolute;inset:0;background:linear-gradient(180deg,#8a8a8a 0%,var(--hero-light) 45%,var(--hero-dark) 100%)}
.hero-title{position:absolute;top:62px;width:100%;text-align:center;font-family:"Nunito",sans-serif;font-weight:900;font-size:30px;color:var(--brand);
  text-shadow:2px 0 0 #fff,-2px 0 0 #fff,0 2px 0 #fff,0 -2px 0 #fff,1.5px 1.5px 0 #fff,-1.5px -1.5px 0 #fff,1.5px -1.5px 0 #fff,-1.5px 1.5px 0 #fff}
.hero-sub{position:absolute;top:105px;width:100%;text-align:center;font-family:"Lato",sans-serif;font-size:17px;line-height:21px;color:var(--white)}
.quote-btn{position:absolute;left:397px;top:216px;width:172px;height:38px;display:block;text-decoration:none}
.quote-bar{position:absolute;left:0;width:172px;height:6px;border-radius:3px;background:linear-gradient(90deg,#f39a2b,#e8d634,#7fc241,#3a8fd0,#6a4ca0,#d6458c)}
.quote-bar.top{top:0}
.quote-bar.bottom{top:32px}
.quote-label{position:absolute;top:11px;left:0;width:100%;text-align:center;font-family:"Lato",sans-serif;font-size:12px;line-height:15px;color:var(--white)}

.intro{position:absolute;top:497px;width:1000px;text-align:center}
.intro p{margin-top:3px;font-size:14px;line-height:17px;color:var(--brand);letter-spacing:.2px}

.service{position:absolute;width:200px;text-align:center}
.service .disc{width:95px;height:95px;border-radius:50%;background:var(--brand-soft);margin:0 auto;display:flex;align-items:center;justify-content:center}
.service h3{font-weight:400;font-size:14px;margin-top:12px;color:var(--brand);letter-spacing:.2px}

.quote-section{position:absolute;top:931px;left:0;width:1000px;height:241px;background:var(--brand);color:var(--white)}
.quote-section h2{position:absolute;top:15px;width:100%;text-align:center;font-weight:400;font-size:15px;letter-spacing:.2px}
.quote-section .lead{position:absolute;top:46px;width:100%;text-align:center;font-size:10px;line-height:15px}
.field{position:absolute;top:90px;height:21px;width:117px;background:var(--white);font-size:9px;color:#8a8aa8;padding:4px 11px}
.field.message{top:118px;left:248px;width:508px;height:83px;padding-top:8px}
.send{position:absolute;left:692px;top:207px;width:64px;height:20px;background:var(--white);color:var(--brand);font-size:10px;text-align:center;line-height:20px}

.site-footer{position:absolute;top:1180px;width:1000px;text-align:center;font-size:9px;color:var(--brand)}
</style>
</head>
<body>

<header class="site-header">
  <div class="brand"><span class="brand-dot"></span><span class="brand-name">Trelvix</span></div>
  <div class="contact">
    <div class="contact-row">
      <svg width="11" height="11" viewBox="0 0 24 24"><path fill="#353896" d="M6.6 10.8a15 15 0 0 0 6.6 6.6l2.2-2.2c.3-.3.7-.4 1-.2 1.1.4 2.3.6 3.6.6.6 0 1 .4 1 1V20c0 .6-.4 1-1 1A17 17 0 0 1 3 4c0-.6.4-1 1-1h3.5c.6 0 1 .4 1 1 0 1.3.2 2.5.6 3.6.1.3 0 .7-.2 1z"/></svg>
      <span>07 555 0188.</span>
    </div>
    <div class="contact-row">
      <svg width="11" height="14" viewBox="0 0 24 30"><path fill="#353896" d="M12 0a10 10 0 0 0-10 10c0 7.5 10 20 10 20s10-12.5 10-20A10 10 0 0 0 12 0zm0 14a4 4 0 1 1 0-8 4 4 0 0 1 0 8z"/></svg>
      <span>4/27HallowayRoad-<br>Fenmere-MarlowBay</span>
    </div>
  </div>
</header>

<nav class="main-nav">
  <ul>
    <li><a class="current" href="#">Home</a></li>
    <li><a href="#">About</a></li>
    <li><a href="#">Photocopying</a></li>
    <li><a href="#">Printing</a></li>
    <li><a href="#">Laminating</a></li>
    <li><a href="#">Businesscards</a></li>
    <li><a href="#">Typingservices</a></li>
    <li><a href="#">Photoprinting</a></li>
    <li><a href="#">Passportphotos</a></li>
    <li><a href="#">Filmprocessing</a></li>
    <li><a href="#">Imagerestoration</a></li>
    <li><a class="lower" href="#">printersupplies</a></li>
    <li><a class="lower" href="#">freequote</a></li>
    <li><a class="lower" href="#">contact</a></li>
  </ul>
</nav>

<section class="hero">
  <div class="hero-photo" role="img" aria-label="Photo of printed brochures and glossy magazine spreads fanned out on a white surface"></div>
  <h1 class="hero-title">“Duplication is our vocation”</h1>
  <p class="hero-sub">Professional photocopying-digital &amp; film<br>processing, design and printing</p>
  <a class="quote-btn" href="#"><span class="quote-bar top"></span><span class="quote-label">REQUEST A QUOTE</span><span class="quote-bar bottom"></span></a>
</section>

<section class="intro">
  <svg width="44" height="36" viewBox="0 0 44 36"><rect x="2" y="4" width="40" height="30" fill="none" stroke="#8cc63f" stroke-width="3"/><g stroke="#8cc63f" stroke-width="2.5"><line x1="8" y1="1" x2="8" y2="7"/><line x1="14" y1="1" x2="14" y2="7"/><line x1="20" y1="1" x2="20" y2="7"/><line x1="26" y1="1" x2="26" y2="7"/><line x1="32" y1="1" x2="32" y2="7"/><line x1="38" y1="1" x2="38" y2="7"/><line x1="9" y1="14" x2="35" y2="14"/><line x1="9" y1="20" x2="35" y2="20"/><line x1="9" y1="26" x2="35" y2="26"/></g></svg>
  <p>Digital printing, laminating and photocopying<br>services throughout Marlow Bay</p>
</section>

<div class="service" style="left:174px;top:607px">
  <div class="disc"><svg width="56" height="50" viewBox="0 0 56 50"><g fill="#8cc63f"><rect x="8" y="22" width="34" height="26"/><rect x="2" y="28" width="8" height="3"/><rect x="40" y="28" width="10" height="3"/><circle cx="40" cy="6" r="5"/><rect x="34" y="12" width="12" height="16" rx="3"/><polygon points="12,20 30,10 32,14 16,22"/></g></svg></div>
  <h3>Photocopying</h3>
</div>
<div class="service" style="left:404px;top:607px">
  <div class="disc"><svg width="58" height="44" viewBox="0 0 58 44"><g fill="#8cc63f"><rect x="4" y="2" width="34" height="10"/><rect x="4" y="14" width="34" height="28"/><rect x="40" y="18" width="16" height="3" transform="rotate(-15 40 18)"/><rect x="40" y="25" width="16" height="3" transform="rotate(-15 40 25)"/><rect x="40" y="32" width="16" height="3" transform="rotate(-15 40 32)"/></g><rect x="10" y="22" width="22" height="4" fill="#ececf8"/></svg></div>
  <h3>Digital printing</h3>
</div>
<div class="service" style="left:638px;top:607px">
  <div class="disc"><svg width="60" height="52" viewBox="0 0 60 52"><circle cx="26" cy="26" r="24" fill="#8cc63f"/><g fill="#ececf8"><circle cx="26" cy="12" r="6"/><circle cx="26" cy="40" r="6"/><circle cx="12" cy="26" r="6"/><circle cx="40" cy="26" r="6"/><circle cx="26" cy="26" r="3"/></g><path d="M44 46 C56 40 60 20 52 8" fill="none" stroke="#8cc63f" stroke-width="4"/></svg></div>
  <h3>Film processing</h3>
</div>
<div class="service" style="left:176px;top:772px">
  <div class="disc"><svg width="56" height="40" viewBox="0 0 56 40"><rect x="2" y="2" width="52" height="36" fill="none" stroke="#8cc63f" stroke-width="3"/><g fill="#8cc63f"><circle cx="15" cy="14" r="5"/><path d="M7 32 q8-14 16 0z"/><rect x="27" y="10" width="22" height="3"/><rect x="27" y="17" width="22" height="3"/><rect x="27" y="24" width="22" height="3"/></g></svg></div>
  <h3>Business cards</h3>
</div>
<div class="service" style="left:402px;top:772px">
  <div class="disc"><svg width="58" height="48" viewBox="0 0 58 48"><g fill="#8cc63f"><rect x="14" y="2" width="30" height="10"/><rect x="2" y="14" width="54" height="20" rx="3"/><rect x="12" y="30" width="34" height="16"/></g><g fill="#ececf8"><rect x="16" y="34" width="26" height="3"/><rect x="16" y="40" width="20" height="3"/></g></svg></div>
  <h3>Photo printing</h3>
</div>
<div class="service" style="left:636px;top:772px">
  <div class="disc"><svg width="40" height="50" viewBox="0 0 40 50"><rect x="4" y="2" width="34" height="46" fill="#8cc63f"/><g stroke="#8cc63f" stroke-width="2"><line x1="1" y1="6" x2="6" y2="6"/><line x1="1" y1="12" x2="6" y2="12"/><line x1="1" y1="18" x2="6" y2="18"/><line x1="1" y1="24" x2="6" y2="24"/><line x1="1" y1="30" x2="6" y2="30"/><line x1="1" y1="36" x2="6" y2="36"/><line x1="1" y1="42" x2="6" y2="42"/></g><rect x="14" y="10" width="18" height="9" fill="#ececf8"/></svg></div>
  <h3>Laminating &amp; Binding</h3>
</div>

<section class="quote-section">
  <h2>Get a free quote…or talk to our team about your requirements</h2>
  <p class="lead">Please fill out the form below and we will contact you with in a day.<br>You can now upload and send us your file for a free quote..</p>
  <div class="field" style="left:248px">first name</div>
  <div class="field" style="left:380px">Number</div>
  <div class="field" style="left:509px">last name</div>
  <div class="field" style="left:639px">Email</div>
  <div class="field message">Message</div>
  <div class="send">SEND</div>
</section>

<footer class="site-footer">Copyright © 2015 trelvix.example</footer>

</body>
</html>
```